Pathways to Brightmoor Land Ventures

size of the ad - 8”x 10.75" plus 0.25" bleed
I would like an ad for a magazine that will stand out and make people want to read the ad.
The ad should not be crowded and people reading the ad will be able to read the text.
I would like it to be a creative and modern-day design.
the list of topics should not be the focus of the ad.
the text is attached.
If you decide to use people in the ad then please no ladies.
please note that leave over 1 inch for the bottom of the footer

```html
<!DOCTYPE html>
<html lang="en">
<head>
<meta charset="UTF-8">
<title>Real Estate Course – Pathways to Brightmoor Land Ventures</title>
<link rel="stylesheet" href="https://fonts.googleapis.com/css2?family=DM+Serif+Display&family=Lora:wght@400;500;600;700&family=Montserrat:wght@600&display=swap">
<style>
  :root {
    --navy: #172537;
    --navy-deep: #111c2b;
    --banner: #17345e;
    --yellow: #f4e61c;
    --white: #ffffff;
    --ink: #1b2230;
    --rule: rgba(255,255,255,0.22);
    --backdrop: #ffffff;
  }
  * { margin: 0; padding: 0; box-sizing: border-box; }
  html, body { width: 1200px; height: 1200px; overflow: hidden; background: var(--backdrop); }
  .ad {
    position: absolute; left: 136px; top: 0;
    width: 927px; height: 1200px;
    background: var(--white);
    overflow: hidden;
  }
  .ad-body {
    position: absolute; left: 0; top: 0;
    width: 927px; height: 1091px;
    background: var(--navy);
  }
  .hero-photo {
    position: absolute; left: 0; top: 0; width: 927px; height: 520px;
    background:
      radial-gradient(ellipse 260px 200px at 640px 260px, rgba(120,150,185,0.35), transparent 70%),
      radial-gradient(ellipse 330px 300px at 620px 200px, #2c3e55 0%, transparent 75%),
      linear-gradient(180deg, var(--navy-deep) 0%, #1d2d42 55%, var(--navy) 100%);
  }
  .title {
    position: absolute; left: 63px; top: 246px;
    font-family: "DM Serif Display", serif;
    color: var(--white);
    font-size: 93px; line-height: 90px; letter-spacing: -1px;
  }
  .rule { position: absolute; left: 63px; height: 1px; background: var(--rule); }
  .rule-top { top: 430px; width: 665px; }
  .rule-mid { top: 476px; width: 736px; }
  .subtitle, .tagline {
    position: absolute; left: 63px;
    font-family: "Montserrat", sans-serif; font-weight: 600;
    color: var(--yellow); text-transform: uppercase; white-space: nowrap;
  }
  .subtitle { top: 438px; font-size: 22.5px; }
  .tagline { top: 487px; font-size: 18.5px; }
  .topics-heading {
    position: absolute; left: 63px; top: 572px;
    font-family: "DM Serif Display", serif; color: var(--white);
    font-size: 40px; line-height: 44px;
    padding-bottom: 4px; border-bottom: 2px solid var(--white);
  }
  .topics { position: absolute; left: 63px; top: 654px; list-style: none; }
  .topics li {
    display: flex; align-items: center; height: 38px;
    font-family: "Lora", serif; font-weight: 500;
    color: var(--white); font-size: 22.5px;
  }
  .topics svg { width: 20px; height: 20px; margin-right: 15px; flex: none; }
  .session-card {
    position: absolute; left: 535px; top: 580px;
    width: 315px; height: 422px;
    background: var(--white); border-radius: 16px; overflow: hidden;
    text-align: center; font-family: "Lora", serif; color: var(--ink);
  }
  .card-banner { position: absolute; left: 0; top: 0; width: 315px; height: 106px; }
  .location {
    position: absolute; left: 0; right: 0; top: 22px;
    font-family: "DM Serif Display", serif; color: var(--white);
    font-size: 46px; line-height: 56px;
  }
  .sessions { position: absolute; left: 0; right: 0; top: 108px; }
  .sessions-count { font-weight: 700; font-size: 35px; line-height: 40px; }
  .sessions-note { font-weight: 500; font-size: 21px; line-height: 22px; }
  .start-date { font-weight: 700; font-size: 27px; line-height: 34px; margin-top: 2px; }
  .scholarships { font-weight: 500; font-size: 21px; line-height: 24px; }
  .early-bird {
    position: absolute; left: 0; top: 254px; width: 315px; height: 40px;
    background: var(--banner); color: var(--yellow);
    font-weight: 600; font-size: 24px; line-height: 40px;
  }
  .audience {
    position: absolute; left: 0; right: 0; top: 300px;
    color: var(--banner); font-weight: 500; font-size: 21px; line-height: 25.5px;
  }
</style>
</head>
<body>
  <main class="ad">
    <section class="ad-body">
      <div class="hero-photo" role="img" aria-label="Photo of a businessman in a suit holding his hands protectively above and below a glowing house outline"></div>

      <h1 class="title">REAL ESTATE<br>COURSE</h1>
      <div class="rule rule-top"></div>
      <p class="subtitle">Pathways to Brightmoor Land Ventures</p>
      <div class="rule rule-mid"></div>
      <p class="tagline">Investing in knowledge is investing in opportunities.</p>

      <h2 class="topics-heading">Topics: partial listing</h2>
      <ul class="topics">
        <li><svg viewBox="0 0 20 20"><path d="M17.5 8.2A7.6 7.6 0 1 1 13.4 3.1" fill="none" stroke="#fff" stroke-width="1.5" stroke-linecap="round"/><path d="M6.4 9.6l3 3 8-8" fill="none" stroke="#fff" stroke-width="1.5" stroke-linecap="round" stroke-linejoin="round"/></svg>Real estate investment strategies</li>
        <li><svg viewBox="0 0 20 20"><path d="M17.5 8.2A7.6 7.6 0 1 1 13.4 3.1" fill="none" stroke="#fff" stroke-width="1.5" stroke-linecap="round"/><path d="M6.4 9.6l3 3 8-8" fill="none" stroke="#fff" stroke-width="1.5" stroke-linecap="round" stroke-linejoin="round"/></svg>Due diligence</li>
        <li><svg viewBox="0 0 20 20"><path d="M17.5 8.2A7.6 7.6 0 1 1 13.4 3.1" fill="none" stroke="#fff" stroke-width="1.5" stroke-linecap="round"/><path d="M6.4 9.6l3 3 8-8" fill="none" stroke="#fff" stroke-width="1.5" stroke-linecap="round" stroke-linejoin="round"/></svg>Financing</li>
        <li><svg viewBox="0 0 20 20"><path d="M17.5 8.2A7.6 7.6 0 1 1 13.4 3.1" fill="none" stroke="#fff" stroke-width="1.5" stroke-linecap="round"/><path d="M6.4 9.6l3 3 8-8" fill="none" stroke="#fff" stroke-width="1.5" stroke-linecap="round" stroke-linejoin="round"/></svg>Underwriting</li>
        <li><svg viewBox="0 0 20 20"><path d="M17.5 8.2A7.6 7.6 0 1 1 13.4 3.1" fill="none" stroke="#fff" stroke-width="1.5" stroke-linecap="round"/><path d="M6.4 9.6l3 3 8-8" fill="none" stroke="#fff" stroke-width="1.5" stroke-linecap="round" stroke-linejoin="round"/></svg>Property management</li>
        <li><svg viewBox="0 0 20 20"><path d="M17.5 8.2A7.6 7.6 0 1 1 13.4 3.1" fill="none" stroke="#fff" stroke-width="1.5" stroke-linecap="round"/><path d="M6.4 9.6l3 3 8-8" fill="none" stroke="#fff" stroke-width="1.5" stroke-linecap="round" stroke-linejoin="round"/></svg>Real estate Legal basics</li>
        <li><svg viewBox="0 0 20 20"><path d="M17.5 8.2A7.6 7.6 0 1 1 13.4 3.1" fill="none" stroke="#fff" stroke-width="1.5" stroke-linecap="round"/><path d="M6.4 9.6l3 3 8-8" fill="none" stroke="#fff" stroke-width="1.5" stroke-linecap="round" stroke-linejoin="round"/></svg>Sourcing deals</li>
        <li><svg viewBox="0 0 20 20"><path d="M17.5 8.2A7.6 7.6 0 1 1 13.4 3.1" fill="none" stroke="#fff" stroke-width="1.5" stroke-linecap="round"/><path d="M6.4 9.6l3 3 8-8" fill="none" stroke="#fff" stroke-width="1.5" stroke-linecap="round" stroke-linejoin="round"/></svg>Syndication</li>
        <li><svg viewBox="0 0 20 20"><path d="M17.5 8.2A7.6 7.6 0 1 1 13.4 3.1" fill="none" stroke="#fff" stroke-width="1.5" stroke-linecap="round"/><path d="M6.4 9.6l3 3 8-8" fill="none" stroke="#fff" stroke-width="1.5" stroke-linecap="round" stroke-linejoin="round"/></svg>Dealing with brokers</li>
        <li><svg viewBox="0 0 20 20"><path d="M17.5 8.2A7.6 7.6 0 1 1 13.4 3.1" fill="none" stroke="#fff" stroke-width="1.5" stroke-linecap="round"/><path d="M6.4 9.6l3 3 8-8" fill="none" stroke="#fff" stroke-width="1.5" stroke-linecap="round" stroke-linejoin="round"/></svg>Tax fundamentals</li>
      </ul>

      <aside class="session-card">
        <svg class="card-banner" viewBox="0 0 315 106" aria-hidden="true">
          <path d="M0 0 H315 V2 Q282 10 282 38 L280 80 L160 104 L40 80 L40 38 Q40 10 0 2 Z" fill="#17345e"/>
        </svg>
        <div class="location">LARKFIELD</div>
        <div class="sessions">
          <div class="sessions-count">10 -Tuesday</div>
          <div class="sessions-note">evenings sessions</div>
          <div class="start-date">Starting Feb.28</div>
          <div class="scholarships">Limited Partial Scholarships</div>
        </div>
        <div class="early-bird">Early Bird Special</div>
        <p class="audience">For those that started or<br>would like to go into<br>real estate</p>
      </aside>
    </section>
  </main>
</body>
</html>
```